Cocktail Menu for my Breakfast Cafe

I would like a simple drink menu designed. I have uploaded the info of names and prices as well as our restaurant logo - We are an old meets new kind of theme - lots of antiques in our restaurant with buffalo heads - wood everywhere. I would just like something simple and rustic looking with a modern twist - the colors that I would like are neutral tones - browns/woods / Taupes etc

Target Market(s)

Variety - families and trendy hipsters on the weekend and Business People during the week

Industry/Entity Type

Cafe

Font styles to use
Serif

Colors

Designer to choose colors to be used in the design.

Requirements
Must have
• must fit on 127 X 178 paper - it will be a table tent menu so there will need to be a front and back design - The front should have the entire drink menu and the back can just be a solid color or maybe something with our logo
Nice to have
• Traditional with a modern twist
• Saloon style
• wood motif perhaps?
Should not have
• I'm pretty flexible with ideas

```html
<!DOCTYPE html>
<html lang="en">
<head>
<meta charset="utf-8">
<title>Wet Your Whistle – Drink Menu</title>
<link rel="stylesheet" href="https://fonts.googleapis.com/css2?family=Alfa+Slab+One&family=IM+Fell+English+SC&family=IM+Fell+English&display=swap">
<style>
  :root {
    --paper: #e8dec9;
    --paper-dark: #d6c8ad;
    --ink: #2a2119;
    --ink-soft: #3b3026;
    --rule: #3a3027;
    --badge: #9c8f7c;
    --art-light: #cbbd9f;
    --art-dark: #5a4a3a;
  }
  * { margin: 0; padding: 0; box-sizing: border-box; }
  html, body { width: 857px; height: 1200px; overflow: hidden; background: var(--paper); }
  .menu {
    position: relative;
    width: 857px; height: 1200px;
    background: radial-gradient(ellipse at 60% 40%, #efe6d4 0%, var(--paper) 55%, var(--paper-dark) 100%);
    color: var(--ink);
    overflow: hidden;
  }
  .menu-title {
    position: absolute; left: 52px; top: 52px;
    font-family: "Alfa Slab One", serif;
    font-weight: 400;
    font-size: 74px; line-height: 72px;
    letter-spacing: 1px;
    color: var(--ink);
    transform: scaleX(0.86); transform-origin: left top;
  }
  .hero-art {
    position: absolute; left: 0; top: 185px;
    width: 450px; height: 930px;
    background: radial-gradient(ellipse at 30% 40%, var(--art-dark) 0%, #8a7760 45%, var(--art-light) 80%, transparent 100%);
    opacity: 0.75;
  }
  .drink { position: absolute; left: 478px; width: 312px; }
  .drink-header {
    position: relative;
    border-top: 1.5px solid var(--rule);
    border-bottom: 1.5px solid var(--rule);
    border-left: 1.5px solid var(--rule);
    padding-left: 22px;
    display: flex; align-items: center;
  }
  .drink-number {
    position: absolute; left: -9px; top: 50%;
    width: 17px; height: 17px; margin-top: -8px;
    border-radius: 50%;
    background: var(--badge);
    color: #efe6d4;
    font-family: "IM Fell English", serif;
    font-size: 11px; line-height: 17px; text-align: center;
  }
  .drink-name {
    font-family: "IM Fell English SC", serif;
    font-size: 40px; line-height: 44px;
    color: var(--ink);
  }
  .ingredients {
    margin-top: 26px; padding-left: 6px;
    list-style: none;
    font-family: "IM Fell English SC", serif;
    font-size: 14px; line-height: 19px;
    font-weight: 700;
    color: var(--ink-soft);
    text-transform: lowercase;
  }
  .prices {
    display: flex; align-items: baseline;
    padding-left: 20px; margin-top: 4px;
    font-family: "IM Fell English", serif;
    color: var(--ink);
  }
  .size { font-family: "IM Fell English SC", serif; font-size: 12px; margin-right: 10px; }
  .amount { font-size: 22px; }
  .prices .gap { width: 40px; }
  .prices .alt { margin-left: 0; }
</style>
</head>
<body>
<main class="menu">
  <h1 class="menu-title">WET YOUR<br>WHISTLE</h1>
  <div class="hero-art" role="img" aria-label="Engraved illustration of a shaggy highland buffalo head beside a hurricane glass and a cocktail glass with fruit garnish"></div>

  <section class="drink" style="top:36px;">
    <div class="drink-header" style="height:72px;"><span class="drink-number">1</span><h2 class="drink-name">Simple Ceasar</h2></div>
    <ul class="ingredients"><li>Vodka</li><li>Clamvine</li><li>Worcestershire</li><li>Firebrand</li><li>Pickled Asparagus</li></ul>
    <div class="prices"><span class="size">1 oz</span><span class="amount">7.00</span><span class="gap"></span><span class="size">Buffalo Size</span><span class="amount">11.00</span></div>
  </section>

  <section class="drink" style="top:286px;">
    <div class="drink-header" style="height:126px;"><span class="drink-number">2</span><h2 class="drink-name">Someone Spiked<br>My Juice!</h2></div>
    <ul class="ingredients"><li>Vodka</li><li>Orange Juice</li></ul>
    <div class="prices"><span class="size">1 oz</span><span class="amount">6.00</span><span class="gap"></span><span class="size">Buffalo Size</span><span class="amount">10.00</span></div>
  </section>

  <section class="drink" style="top:530px;">
    <div class="drink-header" style="height:124px;"><span class="drink-number">3</span><h2 class="drink-name">Bramley's N<br>Coffee</h2></div>
    <ul class="ingredients"><li>Bramley's Liqueur</li><li>Coffee</li></ul>
    <div class="prices"><span class="amount">6.00</span></div>
  </section>

  <section class="drink" style="top:772px;">
    <div class="drink-header" style="height:74px;"><span class="drink-number">4</span><h2 class="drink-name">Madame Mimosa!</h2></div>
    <ul class="ingredients"><li>Prosecco</li><li>Orange Juice</li><li>Raspberries</li></ul>
    <div class="prices"><span class="amount">7.00</span></div>
  </section>

  <section class="drink" style="top:978px;">
    <div class="drink-header" style="height:72px;"><span class="drink-number">5</span><h2 class="drink-name">Local Brew</h2></div>
    <ul class="ingredients"><li>Hamlet Blonde</li><li>Kettlewhistle</li><li>Grist Lane Organic</li></ul>
    <div class="prices"><span class="amount">6.00</span></div>
  </section>
</main>
</body>
</html>
```